Postcard, Logo, and Website Design for Direct to Consumer Personal Bankruptcy Service

We are launching a bankruptcy legal practice. Our postcard design will be mailed to prospective clients who have already been sued by their credit card companies.

We would like people to glean from the post card that they can call to set up a no-fee consultation, or to phone our offices, where our receptionist can aid them in setting up a no-fee consultation.

Logo should be professional, but not overly stuffy.

Website copy can be added later, but most important is a space where people can fill out there info so we can reach out to them.

Pertinent info that should be on postcard

Name: Lakeshore Fresh Start Legal
Phone: 616-372-5819
Website: LFSLegalAid.com

Rough ideas that we've tossed around include the following (but use your own judgement - we're counting on you for creativity):

Creditors Calling?
Mountain of Debt?
Getting Sued?

We can help!

Target Market(s)

People who are thinking about bankruptcy and have already been sued

Industry/Entity Type

Financial Service

Logo Text

Lakeshore Fresh Start Legal

Number of Pages Required

1 page

Font styles to use
Sans Serif

Colors

Designer to choose colors to be used in the design.

Requirements
Must have
• Space for info about bankruptcy process
• Space for user to submit info

```html
<!DOCTYPE html>
<html lang="en">
<head>
<meta charset="utf-8">
<title>Lakeshore Fresh Start Legal – Postcard</title>
<link rel="stylesheet" href="https://fonts.googleapis.com/css2?family=Roboto+Condensed:wght@700&family=Open+Sans:wght@400;600&display=swap">
<style>
  :root {
    --page-bg: #2a2a2a;
    --navy: #145a83;
    --blue: #1591cf;
    --blue-deep: #0d5e8e;
    --silver-light: #f4f4f4;
    --silver-mid: #d6d7d9;
    --silver-dark: #b9bbbe;
    --white: #ffffff;
    --ink: #333333;
    --photo-top: #5a3a24;
    --photo-mid: #c9c3b0;
    --photo-low: #4a2c1a;
  }
  * { margin: 0; padding: 0; box-sizing: border-box; }
  html, body { width: 1000px; height: 1200px; overflow: hidden; }
  body { background: var(--page-bg); position: relative; font-family: "Open Sans", sans-serif; }

  .card { position: absolute; left: 99px; width: 802px; height: 516px; overflow: hidden; background: var(--white); }
  .card-front { top: 51px; }
  .card-back { top: 634px; }
  .card svg.shapes { position: absolute; inset: 0; }

  .front-title {
    position: absolute; left: 40px; top: 48px;
    font-family: "Roboto Condensed", sans-serif; font-weight: 700;
    font-size: 38px; color: var(--navy); letter-spacing: 0.2px;
  }
  .front-rule { position: absolute; left: 40px; top: 99px; width: 430px; height: 2px;
    background: linear-gradient(90deg, transparent, var(--navy) 20%, var(--navy) 80%, transparent); }
  .logo-slot {
    position: absolute; left: 574px; top: 46px; width: 190px;
    font-family: "Open Sans", sans-serif; font-weight: 600; font-size: 28px;
    line-height: 40px; color: var(--blue); text-align: center;
  }

  .back-title {
    position: absolute; left: 26px; top: 22px;
    font-family: "Roboto Condensed", sans-serif; font-weight: 700;
    font-size: 31px; color: var(--white);
  }
  .back-rule { position: absolute; left: 26px; top: 70px; width: 345px; height: 1px;
    background: linear-gradient(90deg, rgba(255,255,255,.7), rgba(255,255,255,.1)); }
  .back-copy { position: absolute; left: 26px; top: 80px; width: 350px; color: var(--white); font-size: 11.6px; line-height: 16.3px; }
  .back-copy p { margin-bottom: 14px; }
  .pain-points { list-style: none; margin-top: -2px; }
  .pain-points li { position: relative; padding-left: 14px; margin-bottom: 5px; }
  .pain-points li::before { content: ""; position: absolute; left: 1px; top: 6px; width: 5px; height: 5px; border-radius: 50%; background: var(--white); }

  .help-band { position: absolute; left: 0; top: 336px; width: 441px; height: 66px; }
  .help-text {
    position: absolute; left: 0; top: 340px; width: 400px; text-align: center;
    font-family: "Roboto Condensed", sans-serif; font-weight: 700; font-size: 42px; color: var(--navy);
  }
  .call-now { position: absolute; left: 0; top: 410px; width: 426px; text-align: center;
    font-family: "Roboto Condensed", sans-serif; font-weight: 700; font-size: 19px; color: var(--white); }
  .call-rule { position: absolute; left: 113px; top: 437px; width: 200px; height: 1px; background: rgba(255,255,255,.6); }
  .phone { position: absolute; left: 0; top: 438px; width: 426px; text-align: center;
    font-family: "Roboto Condensed", sans-serif; font-weight: 700; font-size: 32px; color: var(--white); }
  .web { position: absolute; left: 0; top: 478px; width: 426px; text-align: center; font-size: 14px; color: var(--white); }
  .web-dot { display: inline-block; width: 13px; height: 13px; border: 2px solid var(--white); border-radius: 50%; vertical-align: -2px; margin-right: 6px; }

  .stamp-box { position: absolute; left: 678px; top: 30px; width: 104px; height: 104px; border: 1px solid #555; }
  .address-line { position: absolute; left: 514px; width: 268px; height: 1px; background: #666; }
</style>
</head>
<body>

<section class="card card-front">
  <svg class="shapes" width="802" height="516" viewBox="0 0 802 516">
    <defs>
      <linearGradient id="photoTone" x1="0" y1="0" x2="0" y2="1">
        <stop offset="0" stop-color="var(--photo-top)"/>
        <stop offset="0.55" stop-color="var(--photo-mid)"/>
        <stop offset="1" stop-color="var(--photo-low)"/>
      </linearGradient>
      <linearGradient id="silver" x1="0" y1="0" x2="1" y2="0">
        <stop offset="0" stop-color="var(--silver-dark)"/>
        <stop offset="0.5" stop-color="var(--silver-light)"/>
        <stop offset="1" stop-color="var(--silver-mid)"/>
      </linearGradient>
    </defs>
    <rect width="802" height="516" fill="url(#photoTone)" role="img" aria-label="Photo of a wooden judge's gavel resting on fanned hundred-dollar bills on a wooden table"/>
    <path d="M0,0 H802 V200 C740,215 680,235 560,215 C420,185 260,150 0,245 Z" fill="var(--blue-deep)"/>
    <path d="M0,0 H802 V150 C740,175 680,190 560,180 C420,160 250,130 0,200 Z" fill="var(--blue)"/>
    <path d="M0,0 H802 V100 C760,125 690,148 600,150 C520,150 470,140 400,140 C250,140 120,150 0,190 Z" fill="url(#silver)"/>
  </svg>
  <h1 class="front-title">Lakeshore Fresh Start Legal</h1>
  <div class="front-rule"></div>
  <div class="logo-slot">YOUR<br>LOGO HERE</div>
</section>

<section class="card card-back">
  <svg class="shapes" width="802" height="516" viewBox="0 0 802 516">
    <defs>
      <linearGradient id="silverBand" x1="0" y1="0" x2="1" y2="0">
        <stop offset="0" stop-color="var(--silver-dark)"/>
        <stop offset="0.45" stop-color="var(--silver-light)"/>
        <stop offset="1" stop-color="var(--silver-mid)"/>
      </linearGradient>
    </defs>
    <path d="M0,0 H468 C395,110 470,330 430,516 H0 Z" fill="var(--blue-deep)"/>
    <path d="M0,0 H440 C370,120 450,320 412,516 H0 Z" fill="var(--blue)"/>
    <path d="M0,336 H437 C440,358 441,380 440,402 H0 Z" fill="url(#silverBand)"/>
  </svg>
  <h2 class="back-title">Lakeshore Fresh Start Legal</h2>
  <div class="back-rule"></div>
  <div class="back-copy">
    <p>Lorem Ipsum is simply dummy text of the printing and typesetting industry. Lorem Ipsum has been the industry's standard dummy text ever since the 1500s, when an unknown printer took a galley of type and scrambled it to make a type specimen book.</p>
    <p>Lorem Ipsum is simply dummy text of the printing and typesetting industry. Lorem Ipsum has been the industry's standard dummy text ever since the 1500s, when an unknown printer took a galley of type and scrambled it to make a type specimen book.</p>
    <ul class="pain-points">
      <li>Creditors Calling?</li>
      <li>Mountain of Debt?</li>
      <li>Getting Sued?</li>
    </ul>
  </div>
  <div class="help-text">We can help!</div>
  <div class="call-now">CALL NOW</div>
  <div class="call-rule"></div>
  <div class="phone">616-372-5819</div>
  <div class="web"><span class="web-dot"></span>www.lfslegalaid.com</div>

  <div class="stamp-box"></div>
  <div class="address-line" style="top:296px"></div>
  <div class="address-line" style="top:341px"></div>
  <div class="address-line" style="top:386px"></div>
</section>

</body>
</html>
```